Pizza Restaurant Needs a New Menu Design

RESTAURANT NAME: The Oven and Barrel House
LOCATION:
- Kyneton, central Victoria Australia
- A small historical country town, with a growing market in visitors from Melbourne coming for food and local activities.
TYPE OF RESTAURANT
Pizza and Pasta restaurant. Modern feel, lots of timber, busy feel.
- Describe the overall restaurant theme/concept
- Ambiance
CLIENTELE:
- Mostly local clientele, but a growing number of tourists also. Local families and young people.
Describe your patrons or your market
OBJECTIVE:
-to give a more modern and professional feel to our menus. They are old and simple and boring.
- hard to read under low light at night.
Why are we updating the old menu?
- What do you like about the old menu that designers should keep or consider when designing
- What do you not like about the old menu?
ADDITIONAL INFORMATION:
www.ovenandbarrelhouse.com.au
https://www.facebook.com/The-Oven-and-Barrel-House-804417362958120/
RESOURCES/ SIZES:
Please find attached all our current menus as requested. With all attachments you will notice 2 of everything. We currently print each menu back to back on white card.
Restaurant 1 and Restaurant 2 - back to back - A3 and then folded
Red Wine and White Wine - back to back A4
Take away 1 and Take away 2 - back to back A4
Dessert - A4 - cut in half
Lunch Menu and Lunch Drink Menu - back to back A4
A3 Takeaway Menu
Thank you :)

```html
<!DOCTYPE html>
<html lang="en">
<head>
<meta charset="utf-8">
<title>Dessert Menu</title>
<link rel="stylesheet" href="https://fonts.googleapis.com/css2?family=Source+Sans+3:ital,wght@0,600;0,700;0,800;1,400;1,600&display=swap">
<style>
  :root {
    --paper: #f7ebc6;
    --paper-light: #faf1d4;
    --ink: #231d1b;
    --ink-soft: #3a2a24;
    --subtitle: #5b3529;
    --flourish: #c13a4f;
    --wave-tan: #efd8b2;
    --wave-pink: #ecd0d4;
    --wave-peach: #ebc9a7;
    --leaf-white: #fdfaf2;
    --leaf-tan: #ecd39c;
  }
  * { margin: 0; padding: 0; box-sizing: border-box; }
  html, body { width: 848px; height: 1200px; overflow: hidden; }
  body {
    position: relative;
    background: radial-gradient(ellipse at 40% 35%, var(--paper-light), var(--paper) 70%);
    font-family: "Source Sans 3", "Myriad Pro", sans-serif;
    color: var(--ink);
  }
  .backdrop { position: absolute; inset: 0; width: 848px; height: 1200px; }

  .menu-half { position: absolute; top: 0; width: 400px; height: 700px; }
  .menu-half--left { left: 0; }
  .menu-half--right { left: 430px; }

  .menu-title {
    position: absolute; top: 32px;
    font-size: 20.7px; font-weight: 800; letter-spacing: 0.2px;
  }
  .menu-half--left .menu-title { left: 58px; }
  .menu-half--right .menu-title { left: 6px; }
  .menu-tagline {
    position: absolute; top: 64px;
    font-size: 17.4px; font-style: italic; font-weight: 600; color: var(--subtitle);
  }
  .menu-half--left .menu-tagline { left: 78px; }
  .menu-half--right .menu-tagline { left: 26px; }

  .flourish-rule {
    position: absolute; left: 24px; width: 346px; height: 10px;
  }
  .flourish-rule--top { top: 110px; }
  .flourish-rule--bottom { top: 653px; left: 34px; }

  .dish-name {
    position: absolute; left: 0; width: 384px; text-align: center;
    font-size: 16.2px; font-weight: 700; white-space: nowrap;
  }
  .dish-note {
    position: absolute; font-size: 13.9px; font-style: italic; color: var(--ink-soft);
    white-space: nowrap;
  }
  .dish-note--center { left: 0; width: 384px; text-align: center; }
</style>
</head>
<body>
  <svg class="backdrop" viewBox="0 0 848 1200" aria-hidden="true">
    <path d="M0 805 C120 770 250 830 330 950 S480 1165 700 1200 L0 1200 Z" fill="var(--wave-tan)"/>
    <path d="M0 1118 C90 1100 205 1120 255 1200 L0 1200 Z" fill="var(--wave-pink)"/>
    <rect x="0" y="1118" width="7" height="82" fill="var(--leaf-white)"/>
    <path d="M690 1200 C740 1165 800 1152 848 1158 L848 1200 Z" fill="var(--wave-peach)"/>
  </svg>

  <svg class="backdrop" viewBox="0 0 848 1200" role="img" aria-label="Soft painted leaf shapes at the page edges">
    <ellipse cx="350" cy="20" rx="70" ry="28" fill="var(--leaf-white)" opacity="0.7"/>
    <ellipse cx="760" cy="22" rx="72" ry="26" fill="var(--leaf-white)" opacity="0.7"/>
    <ellipse cx="840" cy="570" rx="26" ry="80" fill="var(--leaf-tan)" opacity="0.7"/>
    <ellipse cx="838" cy="960" rx="18" ry="80" fill="var(--leaf-white)" opacity="0.8"/>
  </svg>

  <section class="menu-half menu-half--left">
    <h1 class="menu-title">DESSERT MENU</h1>
    <p class="menu-tagline">Desserts are made in-house</p>
    <svg class="flourish-rule flourish-rule--top" viewBox="0 0 346 10" role="img" aria-label="Decorative scroll border"><rect y="4" width="346" height="2" rx="1" fill="var(--flourish)"/></svg>

    <h2 class="dish-name" style="top:159px">STICKY DATE PUDDING - $8.00</h2>
    <p class="dish-note dish-note--center" style="top:186px">with butterscotch sauce, cream and/ or ice cream</p>

    <h2 class="dish-name" style="top:239px">APPLE CRUMBLE - $8.00</h2>
    <p class="dish-note" style="top:266px; left:50px">Juicy apples slices baked with crumble,</p>
    <p class="dish-note" style="top:284px; left:138px">topped with cream and/ or ice cream</p>

    <h2 class="dish-name" style="top:342px">CHOCOLATE MOUSSE - $8.00</h2>
    <p class="dish-note dish-note--center" style="top:372px">Rich creamy chocolate mousse served with cream</p>

    <h2 class="dish-name" style="top:429px; left:8px">ICE CREAM SUNDAE - $8.00 (KIDS SIZE - $6.00)</h2>
    <p class="dish-note" style="top:462px; left:61px">Scoops of Vanilla Ice cream served with</p>
    <p class="dish-note" style="top:480px; left:126px">choice of topping</p>
    <p class="dish-note" style="top:497px; left:61px">Chocolate, Strawberry or Caramel (Sprinkles optional )</p>

    <h2 class="dish-name" style="top:547px">ICE CREAM CONE - $2.00</h2>
    <p class="dish-note dish-note--center" style="top:577px">Scoop of Vanilla Ice Cream in a cone (sprinkles optional)</p>

    <svg class="flourish-rule flourish-rule--bottom" viewBox="0 0 346 10" role="img" aria-label="Decorative scroll border"><rect y="4" width="346" height="2" rx="1" fill="var(--flourish)"/></svg>
  </section>

  <section class="menu-half menu-half--right">
    <h1 class="menu-title">DESSERT MENU</h1>
    <p class="menu-tagline">Desserts are made in-house</p>
    <svg class="flourish-rule flourish-rule--top" viewBox="0 0 346 10" role="img" aria-label="Decorative scroll border"><rect y="4" width="346" height="2" rx="1" fill="var(--flourish)"/></svg>

    <h2 class="dish-name" style="top:159px">STICKY DATE PUDDING - $8.00</h2>
    <p class="dish-note dish-note--center" style="top:186px">with butterscotch sauce, cream and/ or ice cream</p>

    <h2 class="dish-name" style="top:239px">APPLE CRUMBLE - $8.00</h2>
    <p class="dish-note" style="top:266px; left:48px">Juicy apples slices baked with crumble,</p>
    <p class="dish-note" style="top:284px; left:137px">topped with cream and/ or ice cream</p>

    <h2 class="dish-name" style="top:342px">CHOCOLATE MOUSSE - $8.00</h2>
    <p class="dish-note dish-note--center" style="top:372px">Rich creamy chocolate mousse served with cream</p>

    <h2 class="dish-name" style="top:429px; left:15px">ICE CREAM SUNDAE - $8.00 (KIDS SIZE - $6.00)</h2>
    <p class="dish-note" style="top:462px; left:71px">Scoops of Vanilla Ice cream served with</p>
    <p class="dish-note" style="top:480px; left:136px">choice of topping</p>
    <p class="dish-note" style="top:497px; left:71px">Chocolate, Strawberry or Caramel (Sprinkles optional )</p>

    <h2 class="dish-name" style="top:547px">ICE CREAM CONE - $2.00</h2>
    <p class="dish-note dish-note--center" style="top:577px">Scoop of Vanilla Ice Cream in a cone (sprinkles optional)</p>

    <svg class="flourish-rule flourish-rule--bottom" viewBox="0 0 346 10" role="img" aria-label="Decorative scroll border"><rect y="4" width="346" height="2" rx="1" fill="var(--flourish)"/></svg>
  </section>
</body>
</html>
```